Business Card Design/Stationary Design

We would like designers to submit cool, hip business card designs (plus stationary designs) for a new, upstart software development company located in Toronto.
If you have any questions, please email us.
For inspiration on designs:
http://cardmuse.example/cool-business-cards/
http://layoutnotes.example/2008/05/36-cool-business-cards-you-should%E2%80%99ve-seen.html
http://gigharbor.example/general/18-smokin-hot-business-card-designs/

Card info:

Selvakumar (Selv) Nadarasan

Founder and CEO

47 Brindle Court, Suite 311

Toronto, ON M4K 2T8

Phone: 647-512-7730

Mobile: 416-273-5094

Fax: 647-512-7731

Email: selvakumar.nadarasan@mailbrook.example

www.quendrix.example
Updates

Hi everyone,

In terms of all the designs I have seen so far, here is what I like:

1.  I really like the "back" part of this design.  The "front" looks pretty decent as well, but for the "front", look at #2 on this list.  I like that.

http://www.pitchboard.example/image.aspx?imageLocation=1000_10001_2000_image.jpg&type=design300px&whiteLabelCustId=9999

2. "Side 1" of this I like, the front needs to be reworked.

http://www.pitchboard.example/image.aspx?imageLocation=1000_10002_2000_image.png&type=design300px&whiteLabelCustId=9999

3. http://www.pitchboard.example/image.aspx?imageLocation=1000_10003_2000_image.jpg&type=design300px&whiteLabelCustId=9999

4. http://www.pitchboard.example/image.aspx?imageLocation=1000_10004_2000_image.jpg&type=design300px&whiteLabelCustId=9999

Target Market(s)

We are focused on enterprise customers right now, so businesses with a long-term goal of also reaching out to the consumer market as well.

Industry/Entity Type

Software

Requirements
Must have
• Must look cool, ultra-modern, clean and eye-catching. Must incorporate our logo and the colors found in the logo.

```html
<!DOCTYPE html>
<html lang="en">
<head>
<meta charset="utf-8">
<title>Quendrix Technologies Inc. — Letterhead</title>
<link href="https://fonts.googleapis.com/css2?family=Lato:wght@400&display=swap" rel="stylesheet">
<style>
  :root {
    --paper: #ffffff;
    --ink: #1a1a1a;
    --text-grey: #5a5a5a;
    --green-lime: #c6d92e;
    --green-leaf: #8cbf3f;
    --green-teal: #1fb27e;
    --green-olive: #5b7b3a;
  }
  * { margin: 0; padding: 0; box-sizing: border-box; }
  html, body {
    width: 851px;
    height: 1200px;
    overflow: hidden;
    background: var(--paper);
  }
  .letterhead {
    position: relative;
    width: 851px;
    height: 1200px;
    background: var(--paper);
    font-family: "Lato", "Helvetica Neue", Arial, sans-serif;
    overflow: hidden;
  }
  .corner-accent {
    position: absolute;
  }
  .corner-accent--top-left {
    left: 0;
    top: 0;
    width: 175px;
    height: 272px;
    background: radial-gradient(ellipse at 0% 45%,
      rgba(198, 217, 46, 0.55) 0%,
      rgba(140, 191, 63, 0.45) 45%,
      rgba(31, 178, 126, 0.25) 75%,
      rgba(255, 255, 255, 0) 100%);
  }
  .corner-accent--bottom-right {
    right: 0;
    bottom: 0;
    width: 272px;
    height: 375px;
    background: radial-gradient(ellipse at 100% 75%,
      rgba(140, 191, 63, 0.5) 0%,
      rgba(198, 217, 46, 0.45) 45%,
      rgba(31, 178, 126, 0.25) 78%,
      rgba(255, 255, 255, 0) 100%);
  }
  .brand {
    position: absolute;
    left: 588px;
    top: 76px;
    display: flex;
    align-items: center;
    gap: 22px;
  }
  .brand__dot {
    width: 38px;
    height: 38px;
    border-radius: 50%;
    background: var(--green-leaf);
  }
  .brand__name {
    font-size: 33px;
    font-weight: 400;
    color: var(--ink);
    letter-spacing: 0.5px;
    line-height: 1;
  }
  .sender {
    position: absolute;
    left: 52px;
    top: 1046px;
    color: var(--text-grey);
  }
  .sender__company {
    font-size: 13px;
    margin-bottom: 16px;
  }
  .sender__details {
    list-style: none;
    font-size: 11px;
    line-height: 15.6px;
  }
  .sender__label {
    color: var(--green-leaf);
  }
</style>
</head>
<body>
  <main class="letterhead">
    <div class="corner-accent corner-accent--top-left" role="img" aria-label="Decorative green corner accent"></div>

    <header class="brand">
      <span class="brand__dot"></span>
      <span class="brand__name">Quendrix</span>
    </header>

    <footer class="sender">
      <p class="sender__company">Quendrix Technologies Inc.</p>
      <ul class="sender__details">
        <li>47 Brindle Court, Suite 311</li>
        <li>Toronto, ON M4K 2T8</li>
        <li><span class="sender__label">w:</span> www.quendrix.example</li>
        <li><span class="sender__label">e:</span> selvakumar.nadarasan@mailbrook.example</li>
        <li><span class="sender__label">t:</span> 647-512-7730</li>
        <li><span class="sender__label">f:</span> 647-512-7731</li>
      </ul>
    </footer>

    <div class="corner-accent corner-accent--bottom-right" role="img" aria-label="Decorative green corner accent"></div>
  </main>
</body>
</html>
```